Friendly, Professional, Simple Catering Menu

Currently we cater but don't have a take-out menu for customers to order from or see our options and we want to change that. Most of the customers we cater are employees of large and small businesses, we also have some private parties we cater to as well. With this in mind we are looking for a professional looking menu but also to have some personal touch with it. The format should be easy to read and understand. We are looking to hand out this menu to local businesses, schools and offices, and maybe after a few trial runs, our store too. Locally, we have a pretty established name but our options can't be seen by the public and we are looking to make that possible with this catering menu. Originally we were thinking of tri-fold menu, 8.5inx14in, but after seeing some of the work done already we trust the designers to create something they think would be the right fit. We don't want it too large nor too small to ensure it won't be an inconvenience for businesses, it must still stand out enough to grab their attention.
Target Market(s)
Businesses, Schools, Office buildings, and Private parties.
Industry/Entity Type
Catering

```html
<!DOCTYPE html>
<html lang="en">
<head>
<meta charset="utf-8">
<title>Kettle &amp; Bowl Catering Menu</title>
<link rel="stylesheet" href="https://fonts.googleapis.com/css2?family=Open+Sans:wght@400;600&family=Patrick+Hand&display=swap">
<style>
  :root {
    --paper: #fdf3c4;
    --paper-deep: #f9e9a6;
    --accent: #e31d1d;
    --ink: #1f1a14;
    --wood-light: #e9dccb;
    --wood-dark: #cdbba5;
  }
  * { box-sizing: border-box; margin: 0; padding: 0; }
  html, body { width: 1200px; height: 729px; overflow: hidden; }
  body {
    position: relative;
    background: radial-gradient(ellipse at 50% 40%, var(--paper) 0%, var(--paper-deep) 100%);
    font-family: "Open Sans", Arial, sans-serif;
    font-size: 11.9px;
    line-height: 15.6px;
    letter-spacing: -0.15px;
    color: var(--ink);
  }
  h1, h2, h3 { font-size: inherit; font-weight: 400; }

  .column { position: absolute; top: 0; display: flex; flex-direction: column; }
  .col-salads { left: 12px; width: 384px; }
  .col-bar { left: 412px; width: 382px; }
  .col-soups { left: 812px; width: 380px; }

  .panel-title {
    font-family: "Patrick Hand", cursive;
    color: var(--accent);
    font-size: 34px;
    line-height: 38px;
    letter-spacing: 0;
  }
  .col-salads .panel-title { margin-top: 16px; width: 340px; text-align: center; }
  .col-soups .panel-title { margin-top: 14px; text-align: center; }

  .item-name, .sub-head { color: var(--accent); }

  .prices { margin: 4px 0 0 64px; }
  .price-row { display: grid; grid-template-columns: 60px 52px auto; height: 23.5px; align-items: center; }
  .price-row span:nth-child(2) { text-align: right; padding-right: 4px; }
  .price-row span:nth-child(3) { padding-left: 10px; }
  .prices.tight .price-row { height: 18px; }

  .photo-pair { display: flex; gap: 16px; }
  .photo { width: 180px; height: 110px; border-radius: 14px; flex: none; }
  .photo-bowl { background: radial-gradient(circle at 40% 45%, #e6b24a 0%, #b33a22 45%, #7a5a2a 100%); }
  .photo-salad { background: radial-gradient(circle at 50% 50%, #d9c35a 0%, #6f8a2f 50%, #2e2a20 100%); }
  .photo-soup-red { background: radial-gradient(circle at 50% 50%, #e9dfc4 0%, #b8231e 45%, #7c1412 100%); }
  .photo-tomato { background: radial-gradient(circle at 45% 45%, #e4792b 0%, #f3f1ec 55%, #d9d6ce 100%); }
  .photo-chili { background: radial-gradient(circle at 45% 45%, #e8b23c 0%, #6e2212 40%, #eeece7 70%); }

  .pickup-row { display: grid; grid-template-columns: 112px 60px; margin-left: 50px; }

  .wood-floor {
    position: absolute; left: 0; bottom: 0; width: 1200px; height: 31px;
    background: repeating-linear-gradient(90deg, var(--wood-light) 0 58px, var(--wood-dark) 58px 60px);
  }
</style>
</head>
<body>

<section class="column col-salads">
  <h1 class="panel-title">Salads</h1>

  <h2 class="item-name" style="margin-top:16px">Garden Salad</h2>
  <p>Includes: Cucumbers, tomato’s, cheddar cheese, and Ice-Berg lettuce.</p>
  <div class="prices">
    <div class="price-row"><span>Small</span><span>$15.00</span><span>(serves 6-12)</span></div>
    <div class="price-row"><span>Medium</span><span>$30.00</span><span>(serves 13-24)</span></div>
    <div class="price-row"><span>Large</span><span>$45.00</span><span>(serves 25-35)</span></div>
  </div>

  <h2 class="item-name" style="margin-top:6px">Caesar Salad</h2>
  <p>Includes: Croutons, chicken, bacon, parmesan cheese, and Romaine lettuce.</p>
  <div class="prices">
    <div class="price-row"><span>Small</span><span>$20.00</span><span>(serves 6-12)</span></div>
    <div class="price-row"><span>Medium</span><span>$35.00</span><span>(serves 13-24)</span></div>
    <div class="price-row"><span>Large</span><span>$50.00</span><span>(serves 25-35)</span></div>
  </div>

  <h2 class="item-name" style="margin-top:6px">Chef Salad</h2>
  <p>Includes: Feta cheese, blue cheese, bacon, chicken, chopped eggs, tomato’s, Ice-Berg and Romaine lettuce.</p>
  <div class="prices">
    <div class="price-row"><span>Small</span><span>$20.00</span><span>(serves 6-12)</span></div>
    <div class="price-row"><span>Medium</span><span>$35.00</span><span>(serves 13-24)</span></div>
    <div class="price-row"><span>Large</span><span>$50.00</span><span>(serves 25-35)</span></div>
  </div>

  <h2 class="item-name" style="margin-top:4px">Design Your Own Salad</h2>
  <p>Pick one lettuce, one meat, one cheese, up to five toppings, and 2 dressings</p>
  <div class="prices" style="margin-left:68px">
    <div class="price-row"><span>Small</span><span>$25.00</span><span>(serves 6-12)</span></div>
    <div class="price-row"><span>Medium</span><span>$40.00</span><span>(serves 13-24)</span></div>
    <div class="price-row"><span>Large</span><span>$55.00</span><span>(serves 25-35)</span></div>
  </div>

  <div class="photo-pair" style="margin-top:18px">
    <div class="photo photo-salad" role="img" aria-label="Photo of a chef salad bowl with croutons, cheese and ham"></div>
    <div class="photo photo-salad" role="img" aria-label="Photo of a garden salad with cucumbers, tomatoes and cheddar"></div>
  </div>
</section>

<section class="column col-bar">
  <h2 class="sub-head" style="margin-top:17px">The Kettle &amp; Bowl Salad Bar</h2>
  <p>For $150 you will receive a lettuce of your choice, 12 items from our salad bar, and 3 dressings all placed on our own inflatable salad bar! We have a portable salad bar that can fit 12 items, a bowl of lettuce, and 3 dressings. A customer can choose 12 products from our extensive list of options on the salad bar.</p>

  <div class="photo-pair" style="margin-top:22px">
    <div class="photo photo-bowl" role="img" aria-label="Photo of a soup bowl with a side salad and breadsticks"></div>
    <div class="photo photo-soup-red" role="img" aria-label="Photo of a creamy soup in a red bowl with a spoon"></div>
  </div>

  <h2 class="sub-head" style="margin-top:36px">Kettle &amp; Bowl produce!</h2>
  <h3 class="item-name" style="margin-top:5px">Lettuces</h3>
  <p>Romaine, Spinach, and Iceberg.</p>
  <h3 class="item-name" style="margin-top:5px">Meats</h3>
  <p>Chicken, Pepperoni, Bacon, and Ham.</p>
  <h3 class="item-name" style="margin-top:5px">Cheeses</h3>
  <p>Shredded Parmesan Cheese, Feta Cheese, Blue Cheese, and Cheddar Cheese.</p>
  <h3 class="item-name" style="margin-top:5px">Toppings</h3>
  <p>Tomato’s, Olives, Beets, Mushrooms, Peas, Carrots, Onions, Green-Bell Peppers, Cabbage, Brussels Sprouts, Cauliflower, Baby Corn, Cucumbers, Broccoli, Celery, Radishes, Pickles, Pears, Pineapple, Peaches, Oranges, Mixed Fruit, Black Beans, Garbonzo Beans, Kidney Beans, Artichoke, Sweet Pickle, Pepperoncini’s, Halved Pickles, Chow Mein, Croutons, Cranberries, Walnuts, Seeds, Tortilla Strips, Cottage Cheese.</p>
  <h3 class="item-name" style="margin-top:12px">Dressings</h3>
  <p>Ranch, Fat Free Ranch, Caesar, Blue Cheese, Raspberry Vinaigrette, Balsamic Vinaigrette, French dressing, Thousand Island, Spicy Southwest Ranch, Italian, Honey Mustard, Salsa, Olive Oil, and Vinegar.</p>
</section>

<section class="column col-soups">
  <h1 class="panel-title">Soups</h1>

  <h2 class="sub-head" style="margin-top:5px">Kettle &amp; Bowl’s Famous Five</h2>
  <p style="margin-top:5px">Baked Potato with Bacon, Chicken Noodle, Clam Chowder, Creamy Tomato Basil, and Chili</p>
  <h2 class="item-name" style="margin-top:5px">Travelers List:</h2>
  <p style="margin-top:5px">Amazing Corn Chowder, Albondigas (Meatball) Soup, Beef Steak and Noodle, Bistro Spinach Artichoke, Cheeseburger Soup, Cheesy Chicken Noodle, Cheesy Potato with Bacon, Chicken Dumpling Soup, Chicken Enchilada, Chicken Fajita, Chicken Gumbo, Chicken with Wild Rice and Mushroom Soup, Chipotle Chicken Chowder, Classic Cream of</p>

  <div class="photo-pair" style="margin-top:4px">
    <div class="photo photo-tomato" role="img" aria-label="Photo of tomato basil soup in a white cup with a spoon"></div>
    <div class="photo photo-chili" role="img" aria-label="Photo of chili topped with cheddar in a white cup"></div>
  </div>

  <p style="margin-top:10px">Mushroom, Cowboy Campfire Soup, Cream of Asparagus, Cream of Asparagus with Cheese, Cream of Broccoli with Cheese, Fiesta Tortilla Chicken Soup, French Onion Soup, Grandma’s Chicken and Rice Soup, Great Northern Bean and Ham Soup, Hearty Grains and Beef, Italian Wedding Soup, Kickin’ Chicken Noodle, Kickin’ Pepper Jack Broccoli and Potato Soup, Kickin’ Pepper Jack Cheeseburger Soup, Nora’s Lasagna Soup, Manhattan Clam Chowder, Edie’s Mushroom Soup, Mediterranean Veggie Chicken Noodle Soup, Mediterranean Veggie Soup, Mediterranean Veggie Noodle Soup, Normandy Veggie with Cheese Soup, Pumpkin Bisque, Red Beans and Rice Soup, Roasted Red Pepper Bisque, Roasted Red Pepper Bisque with Cheese Tortellini, Royal Bean and Bacon Soup, Stuffed Bell Pepper Soup, Swiss Mushroom Cheeseburger Soup, Tomato Basil with Cheese Tortellini, White Chicken Chili, Wisconsin Cheddar, and Zesty Taco Soup.</p>
  <p style="margin-top:3px">All soups will be listed as the same price</p>
  <div class="prices tight" style="margin:1px 0 0 50px">
    <div class="price-row"><span>Small</span><span>$35.00</span><span>(serves 12-16)</span></div>
    <div class="price-row"><span>Medium</span><span>$45.00</span><span>(serves 17-25)</span></div>
    <div class="price-row"><span>Large</span><span>$70.00</span><span>(serves 26-34)</span></div>
  </div>
  <p style="margin-top:4px">Costumers can also do in store pick up of</p>
  <div class="pickup-row" style="margin-top:2px"><span>½ Gallon of soup</span><span>$17.49</span></div>
  <div class="pickup-row"><span>1 Gallon of soup</span><span>$34.99</span></div>
</section>

<div class="wood-floor" role="img" aria-label="Light wooden plank band"></div>

</body>
</html>
```